Sprinkles & Sniffs 2nd Annual Fundraiser

I am a Realtor sponsoring the 2nd annual fundraiser on behalf of Allies of Marlow Ridge Animal Haven. Like the flyer to be professional yet fun and inviting. Please see the attached file below. The 1st annual flyer was fun but not as professional, modern or inviting as I would have liked it to be.
Target Market(s)
Dog lovers in Ponte Vedra, Ponte Vedra Beach and Nocatee Florida
Logo Text
Needed
Other font styles liked:
- Font that fits the style of the fundraiser
Colors
886aae
abd036
Requirements
Must have
- Please see the attached flyer and photos.
- This will be the 2nd Annual on Saturday, April 27, 2019 from 10AM - 1PM. Same location: Kessler Realty, 418 Harrowgate Blvd. Ponte Vedra FL 32947

```html
<!DOCTYPE html>
<html lang="en">
<head>
<meta charset="utf-8">
<title>Sprinkles &amp; Sniffs – 2nd Annual Doggie Wash</title>
<link rel="stylesheet" href="https://fonts.googleapis.com/css2?family=Arimo:wght@400;700&family=Chewy&display=swap">
<style>
:root{
  --purple:#5655a0;
  --purple-soft:#886aae;
  --green:#abd036;
  --ink:#1c1c1c;
  --paper:#ffffff;
  --mat:#000000;
}
*{box-sizing:border-box;margin:0;padding:0}
html,body{width:928px;height:1200px;overflow:hidden;background:var(--mat)}
.flyer{position:absolute;left:70px;top:90px;width:788px;height:1020px;background:var(--paper);overflow:hidden;font-family:"Arimo",Arial,sans-serif;color:var(--ink)}
.abs{position:absolute}
.support{left:40px;top:24px;font-size:13px}
.support-name{left:40px;top:46px;width:120px;font-size:12px;font-weight:700;color:var(--purple);line-height:1.25}
.art-dog{left:0;top:40px;width:360px;height:620px;background:radial-gradient(ellipse at 55% 40%,#e4e3f2 0%,#f3f3f7 55%,rgba(255,255,255,0) 80%)}
.paw{background:var(--green);border-radius:46% 46% 50% 50%}
.paw-top{left:380px;top:0;width:120px;height:90px;border-radius:0 0 50% 50%}
.paw-left{left:0;top:600px;width:70px;height:120px;border-radius:0 50% 50% 0}
.paw-foot{left:384px;top:968px;width:58px;height:46px}
.photo-wash{left:492px;top:0;width:296px;height:238px;background:linear-gradient(160deg,#9fb6c9,#7d8c6e 55%,#b9b3a6)}
.photo-sign{left:659px;top:215px;width:129px;height:169px;background:linear-gradient(180deg,#8fc0ea,#6d8f5f 70%,#8a8a84)}
.photo-mascot{left:616px;top:373px;width:129px;height:169px;background:linear-gradient(160deg,#d9d3cb,#a0643a 55%,#efefef)}
.photo-greet{left:659px;top:524px;width:129px;height:168px;background:linear-gradient(180deg,#8fbfe4,#6f9a55 55%,#b5a58f)}
.second{left:210px;top:286px;width:380px;text-align:center;font-size:30px;font-weight:700;letter-spacing:.5px;white-space:nowrap}
.title{font-family:"Chewy",cursive;color:var(--purple);font-weight:400;font-size:72px;line-height:1;white-space:nowrap}
.title-1{left:176px;top:322px}
.title-2{left:282px;top:404px}
.subtitle{left:190px;top:500px;width:420px;text-align:center;font-family:"Chewy",cursive;font-size:30px;white-space:nowrap}
.tagline{left:220px;top:546px;width:358px;height:33px;background:var(--green);text-align:center;font-size:24px;font-weight:700;line-height:33px;color:#2a2a2a}
.details{left:170px;top:584px;width:460px;text-align:center;font-size:17px;line-height:18.5px}
.details dt{color:var(--purple);font-weight:700}
.free-head{left:20px;top:702px;width:748px;height:20px;background:var(--purple);color:#fff;text-align:center;font-size:19px;font-weight:700;letter-spacing:9px;line-height:20px}
.free-list{left:20px;top:722px;width:748px;height:56px;background:var(--green);font-size:17px;font-weight:700;color:#222}
.free-list li{position:absolute;list-style:none;white-space:nowrap}
.free-list li::before{content:"";display:inline-block;width:8px;height:8px;border-radius:50%;background:var(--purple);margin-right:5px;vertical-align:2px}
.donate{left:132px;top:778px;width:532px;height:157px;background:var(--purple);color:#fff;text-align:center;border-radius:0 0 60% 60%/0 0 14% 14%}
.donate h2{font-size:19px;font-weight:700;margin-top:10px}
.donate .how{font-size:16px;line-height:18px;margin-top:10px}
.donate .btn{display:inline-block;background:#222;color:#fff;font-weight:700;font-size:15px;padding:2px 9px;border-radius:3px;margin-top:3px}
.donate .note{font-size:13px;line-height:15.5px;margin-top:8px}
.photo-left{left:0;top:768px;width:132px;height:164px;background:linear-gradient(160deg,#e9e4e9,#b98452 55%,#c9c2b4)}
.photo-right{left:664px;top:768px;width:124px;height:164px;background:linear-gradient(160deg,#e6e6ea,#8d7d68 55%,#d65c9a)}
.realtor{left:40px;top:962px;width:130px;text-align:center;font-size:15px;font-weight:700;color:var(--purple)}
.haven{left:464px;top:956px;width:80px;text-align:center;font-size:9.5px;font-weight:700;color:var(--purple);line-height:1.2}
.contact{font-size:11.5px;line-height:13.5px;white-space:nowrap}
.contact b{font-size:12px}
.contact svg{width:9px;height:9px;margin-right:5px;vertical-align:-1px;fill:var(--purple)}
.contact-a{left:164px;top:950px}
.contact-b{left:555px;top:950px}
</style>
</head>
<body>
<main class="flyer">
  <div class="abs art-dog" role="img" aria-label="Line drawing of a dog in a fedora with floating soap bubbles"></div>
  <div class="abs paw paw-top" role="img" aria-label="Green paw print"></div>
  <div class="abs paw paw-left" role="img" aria-label="Green paw print"></div>

  <p class="abs support">In Support of</p>
  <p class="abs support-name">Allies of Marlow Ridge Animal Haven</p>

  <div class="abs photo-wash" role="img" aria-label="Volunteers washing dogs outdoors"></div>
  <div class="abs photo-sign" role="img" aria-label="Balloons and free doggie wash sign by the road"></div>
  <div class="abs photo-mascot" role="img" aria-label="Dog mascot costume waving"></div>
  <div class="abs photo-greet" role="img" aria-label="Mascot greeting a child outside"></div>

  <p class="abs second">SECOND&nbsp;&nbsp;ANNUAL</p>
  <h1>
    <span class="abs title title-1">Sprinkles</span>
    <span class="abs title title-2">&amp; Sniffs</span>
  </h1>
  <p class="abs subtitle">Doggie Wash Extravaganza</p>

  <p class="abs tagline">a family fun event for all ages</p>

  <dl class="abs details">
    <dt>DATE:</dt><dd>Saturday, April 27, 2019</dd>
    <dt>TIME:</dt><dd>10AM - 1PM.</dd>
    <dt>SAME LOCATION:</dt><dd>Kessler Realty, 418 Harrowgate Blvd. Ponte Vedra FL 32947</dd>
  </dl>

  <p class="abs free-head">FREE</p>
  <ul class="abs free-list">
    <li style="left:58px;top:5px">DOGGIE WASH</li>
    <li style="left:252px;top:5px">FOOD &amp; BEVERAGES</li>
    <li style="left:487px;top:5px">VENDORS (give-a-ways)</li>
    <li style="left:176px;top:31px">RAFFLE DRAWINGS</li>
    <li style="left:394px;top:31px">GRAND PRIZE and MORE!</li>
  </ul>

  <section class="abs donate">
    <h2>DONATIONS ARE WELCOME AND MUCH APPRECIATED.</h2>
    <p class="how">To make a donation:<br>www.givepage.org/AMRAH</p>
    <span class="btn">Click: Donate</span>
    <p class="note">All domestic dog breeds from puppies to seniors are invited!<br>Please be sure your furry family member is tolerant<br>of other dogs, crowds and bathing.</p>
  </section>
  <div class="abs photo-left" role="img" aria-label="Woman with her dog beside an event sign"></div>
  <div class="abs photo-right" role="img" aria-label="Shaggy dog in a bandana beside an event sign"></div>

  <p class="abs realtor">Delia Marsh</p>
  <div class="abs contact contact-a">
    <b>DELIA MARSH</b><br>
    <svg viewBox="0 0 10 10"><path d="M5 0a3.5 3.5 0 0 0-3.5 3.5C1.5 6 5 10 5 10s3.5-4 3.5-6.5A3.5 3.5 0 0 0 5 0zm0 5a1.5 1.5 0 1 1 0-3 1.5 1.5 0 0 1 0 3z"/></svg>Kessler Realty Corp., Nocatee<br>
    <svg viewBox="0 0 10 10"><rect x="2" y="0" width="6" height="10" rx="1"/></svg>555-210-4837<br>
    <svg viewBox="0 0 10 10"><rect x="0" y="2" width="10" height="6"/></svg>deliamarsh@kesslerrealtycorp.com
  </div>
  <div class="abs paw paw-foot" role="img" aria-label="Green paw print"></div>
  <p class="abs haven">Allies of Marlow Ridge Animal Haven</p>
  <div class="abs contact contact-b">
    <b>RENEE CALDER</b><br>
    <svg viewBox="0 0 10 10"><path d="M5 0a3.5 3.5 0 0 0-3.5 3.5C1.5 6 5 10 5 10s3.5-4 3.5-6.5A3.5 3.5 0 0 0 5 0zm0 5a1.5 1.5 0 1 1 0-3 1.5 1.5 0 0 1 0 3z"/></svg>Allies of Marlow Ridge Animal Haven<br>
    <svg viewBox="0 0 10 10"><rect x="2" y="0" width="6" height="10" rx="1"/></svg>555-384-9162<br>
    <svg viewBox="0 0 10 10"><rect x="0" y="2" width="10" height="6"/></svg>renee-calder@mailbox.net
  </div>
</main>
</body>
</html>
```